International sports company needs packaging design for color box

We need this box for our yoga mats which we will sell online. This mat is very high quality and 100% environmentally friendly. The yoga mat comes in a stylish yoga bag that will be in the box.

Yoga enthusiasts, athletes, gymnasts, actually all people who do sporting activities and value environmental friendliness will be the contact group

The logo should be visible in any case. The creator is free to choose whether to use only the complete logo or the complete logo with the emblem. In terms of style, it should be reminiscent of a packaging box from Corvane's Zentrix. Be as timeless, modern and elegant as possible. If an environmentally friendly detail can be added, this would certainly be a plus. Color should be black / white / gray.

Target Market(s)

Germany

Requirements
Must have
• Size for the color box should be 13x13x61.5 cm.

```html
<!DOCTYPE html>
<html lang="en">
<head>
<meta charset="utf-8">
<title>Kestrel Yoga Mat – Colour Box</title>
<link href="https://fonts.googleapis.com/css2?family=Varela+Round&family=Josefin+Sans:wght@400;600;700&family=Encode+Sans+Condensed:wght@500;600&display=swap" rel="stylesheet">
<style>
  :root{
    --stage:#3c3c3c;
    --board:#efefef;
    --board-tone:#e4e4e4;
    --ink:#0c0c0c;
    --paper:#ffffff;
    --grey:#555555;
    --copper:#b8784a;
    --leaf:#7cc242;
    --leaf-deep:#3e8a1e;
  }
  *{box-sizing:border-box;margin:0;padding:0}
  html,body{width:1200px;height:810px;overflow:hidden;background:var(--stage)}
  .canvas{position:relative;width:1200px;height:810px}
  .panel{position:absolute;left:100px;width:1000px;height:211px;overflow:hidden}
  .texture{position:absolute;inset:0;background:linear-gradient(135deg,var(--board),var(--board-tone) 60%,var(--board))}

  /* top face */
  .panel--top{top:50px}
  .label{position:absolute;left:0;top:45px;width:610px;height:128px;background:var(--ink);color:var(--paper)}
  .label__mark{position:absolute;left:14px;top:12px;width:118px;height:104px;border:3px solid var(--copper);border-radius:4px;display:flex;align-items:center;justify-content:center;font-family:"Josefin Sans",sans-serif;font-weight:700;font-size:21px;letter-spacing:1px}
  .label__title{position:absolute;left:205px;top:12px;font-family:"Varela Round",sans-serif;font-size:52px;line-height:1}
  .label__tagline{position:absolute;left:245px;top:76px;font-family:"Josefin Sans",sans-serif;font-weight:600;font-size:11.5px}
  .label__desc{position:absolute;left:245px;top:95px;font-family:"Josefin Sans",sans-serif;font-size:8.5px;line-height:1.25}
  .label__size{position:absolute;left:143px;top:108px;font-family:"Josefin Sans",sans-serif;font-size:8.5px}
  .label__thick{position:absolute;left:440px;top:108px;font-family:"Josefin Sans",sans-serif;font-size:8.5px}
  .badge{position:absolute;left:455px;width:42px;height:42px;border-radius:50%;background:var(--leaf);border:3px dotted var(--paper)}
  .badge::after{content:"";position:absolute;inset:9px;border-radius:50%;background:var(--leaf-deep)}
  .features{position:absolute;left:515px;top:20px;list-style:none;font-family:"Encode Sans Condensed",sans-serif;font-weight:600;font-size:9.5px}
  .features li{display:flex;align-items:center;gap:6px;height:22px}
  .features svg{width:16px;height:16px}

  /* side face */
  .panel--side{top:295px}
  .brand{position:absolute;left:30px;top:125px;display:flex;align-items:center;gap:10px;font-family:"Josefin Sans",sans-serif;font-weight:700;font-size:34px;color:var(--ink);letter-spacing:3px}
  .brand__dot{width:22px;height:22px;background:var(--ink)}
  .product{position:absolute;left:240px;top:40px;font-family:"Josefin Sans",sans-serif;color:var(--ink)}
  .product__name{font-family:"Varela Round",sans-serif;font-size:52px;letter-spacing:2px;line-height:1}
  .product__rule{width:270px;height:2px;background:var(--ink);margin:10px 0 6px}
  .product__sub{font-size:22px;letter-spacing:3px;padding-left:18px}
  .copy{position:absolute;font-family:"Encode Sans Condensed",sans-serif;font-weight:600;font-style:italic;font-size:14px;line-height:1.3;color:var(--grey)}
  .copy--left{left:560px;top:40px;width:200px}
  .copy--right{left:800px;top:40px;width:180px}
  .copy--right p+p{margin-top:28px}
  .divider{position:absolute;left:778px;top:30px;width:2px;height:150px;background:var(--grey)}

  /* end face */
  .panel--end{top:540px;left:494px;width:211px}
  .end__band{position:absolute;left:0;right:0;top:55px;height:100px;background:var(--ink);color:var(--paper);display:flex;flex-direction:column;align-items:center;justify-content:center;gap:6px}
  .end__brand{font-family:"Josefin Sans",sans-serif;font-weight:700;font-size:20px;letter-spacing:2px}
  .end__name{font-family:"Varela Round",sans-serif;font-size:16px}
</style>
</head>
<body>
<main class="canvas">

  <section class="panel panel--top" aria-label="Top face">
    <div class="texture" role="img" aria-label="Light grey embossed diamond pattern"></div>
    <div class="label">
      <div class="label__mark">Kestrel</div>
      <h1 class="label__title">Yoga Mat</h1>
      <p class="label__tagline">Connect the mind and body</p>
      <p class="label__desc">High density cushion for joint protection<br>on Hard and Soft surfaces</p>
      <p class="label__size">Dimension- 24″ x 72″</p>
      <p class="label__thick">Thickness - 6 mm</p>
      <span class="badge" style="top:12px" role="img" aria-label="Earth friendly badge"></span>
      <span class="badge" style="top:60px" role="img" aria-label="Phthalates free badge"></span>
      <ul class="features">
        <li><svg viewBox="0 0 16 16"><circle cx="8" cy="8" r="7" fill="none" stroke="#fff" stroke-width="1.3"/><rect x="5.5" y="4" width="5" height="7" rx="2" fill="#fff"/></svg>Ultimate Grip</li>
        <li><svg viewBox="0 0 16 16"><circle cx="8" cy="8" r="7" fill="none" stroke="#fff" stroke-width="1.3"/><path d="M8 3.5 C10 6.5 11 8 11 9.5 A3 3 0 0 1 5 9.5 C5 8 6 6.5 8 3.5Z" fill="#fff"/></svg>Water Resistant</li>
        <li><svg viewBox="0 0 16 16"><circle cx="8" cy="8" r="7" fill="none" stroke="#fff" stroke-width="1.3"/><circle cx="8" cy="5" r="1.5" fill="#fff"/><path d="M4 12 L8 7.5 L12 12Z" fill="#fff"/></svg>Comfort &amp; Support</li>
        <li><svg viewBox="0 0 16 16"><circle cx="8" cy="8" r="7" fill="none" stroke="#fff" stroke-width="1.3"/><path d="M5 11 L11 5 M5 5 L11 11" stroke="#fff" stroke-width="1.5"/></svg>Super Durability</li>
      </ul>
    </div>
  </section>

  <section class="panel panel--side" aria-label="Side face">
    <div class="texture" role="img" aria-label="Light grey embossed diamond pattern"></div>
    <div class="brand"><span class="brand__dot"></span>Kestrel</div>
    <div class="product">
      <h2 class="product__name">Yoga Mat</h2>
      <div class="product__rule"></div>
      <p class="product__sub">Premium Quality</p>
    </div>
    <div class="copy copy--left">
      <p>Connect the mind and body. High density cushion for joint protection on hard and soft surfaces.</p>
      <p>Textured surface side for non-skid resistance, even when moist.</p>
    </div>
    <div class="divider"></div>
    <div class="copy copy--right">
      <p>Light and easy to carry. Carrying strap included.</p>
      <p>Environment friendly and free of phthalates</p>
    </div>
  </section>

  <section class="panel panel--end" aria-label="End face">
    <div class="texture" role="img" aria-label="Light grey embossed diamond pattern"></div>
    <div class="end__band">
      <span class="end__brand">Kestrel</span>
      <span class="end__name">Yoga Mat</span>
    </div>
  </section>

</main>
</body>
</html>
```